I would like a business card to match my truck wrap and logo. I would like the font to match my existing business card please.

Industry/Entity Type

Painter

Contact Information for Business Card

Rodrigo Venaza 801-437-2916 Venazacoatings.utah@brushmail.net
SERVICES - Custom Paint & Stain, Interior & Exterior, Epoxy Coatings / Garage Floors, Cabinet Refinishing, Log Staining and Refinishing.

Requirements
Nice to have
• I would like to have the white and grey line like the bottom of my vehicle wrap, Light Grey to match my truck also.

```html
<!DOCTYPE html>
<html lang="en">
<head>
<meta charset="UTF-8">
<title>Venaza Coatings — Business Card</title>
<link rel="stylesheet" href="https://fonts.googleapis.com/css2?family=Roboto+Slab:wght@400;500;700&display=swap">
<style>
  :root {
    --blue: #1e9ad6;
    --blue-deep: #1170b4;
    --ink: #3d434a;
    --paper: #ffffff;
    --line-grey: #c9cdd2;
    --stage: #e6e9ed;
  }
  * { margin: 0; padding: 0; box-sizing: border-box; }
  html, body { width: 1200px; height: 900px; overflow: hidden; }
  body {
    background: var(--stage);
    font-family: "Roboto Slab", serif;
    display: flex;
    flex-direction: column;
    align-items: center;
    justify-content: center;
    gap: 44px;
  }
  .card {
    position: relative;
    width: 700px;
    height: 400px;
    background: var(--paper);
    box-shadow: 0 4px 18px rgba(0,0,0,0.12);
    overflow: hidden;
  }
  .brand {
    display: flex;
    align-items: center;
    gap: 16px;
    color: var(--blue);
    font-weight: 700;
    text-transform: uppercase;
  }
  .brand-square {
    background: linear-gradient(135deg, var(--blue-deep), var(--blue));
  }
  /* front side */
  .card--front .brand {
    position: absolute;
    left: 60px;
    top: 52px;
    font-size: 34px;
    letter-spacing: 2px;
  }
  .card--front .brand-square { width: 54px; height: 54px; }
  .contact {
    position: absolute;
    left: 330px;
    top: 150px;
  }
  .contact-name {
    color: var(--blue);
    font-size: 26px;
    font-weight: 500;
    text-transform: uppercase;
    margin-bottom: 14px;
  }
  .contact-row {
    display: flex;
    align-items: center;
    gap: 12px;
    color: var(--ink);
    font-size: 16px;
    margin-bottom: 8px;
  }
  .contact-icon {
    width: 26px;
    height: 26px;
    flex: none;
  }
  .services {
    position: absolute;
    left: 60px;
    right: 50px;
    top: 282px;
    color: var(--blue);
    font-size: 14.5px;
    line-height: 1.65;
    text-transform: uppercase;
  }
  .grey-band {
    position: absolute;
    left: 0;
    right: 0;
    bottom: 22px;
    height: 3px;
    background: var(--line-grey);
  }
  /* back side */
  .card--back {
    display: flex;
    align-items: center;
    justify-content: center;
  }
  .card--back .brand { font-size: 46px; letter-spacing: 3px; gap: 22px; }
  .card--back .brand-square { width: 78px; height: 78px; }
</style>
</head>
<body>

  <section class="card card--front" aria-label="Business card front">
    <div class="brand">
      <span class="brand-square"></span>
      <span class="brand-name">Venaza Coatings</span>
    </div>

    <div class="contact">
      <h1 class="contact-name">Rodrigo Venaza</h1>
      <p class="contact-row">
        <svg class="contact-icon" viewBox="0 0 26 26" aria-hidden="true">
          <rect x="1" y="1" width="24" height="24" rx="6" fill="none" stroke="var(--blue)" stroke-width="1.6"/>
          <path d="M9 7c1 0 1.6 2.2 1.6 2.8 0 .8-1.2 1-1 1.8.5 1.8 2 3.3 3.8 3.8.8.2 1-1 1.8-1 .6 0 2.8.6 2.8 1.6 0 1.3-1.4 2.2-2.6 2-4-.6-7.3-3.9-7.9-7.9C7.3 8.9 7.9 7 9 7z" fill="var(--blue)"/>
        </svg>
        <span>801-437-2916</span>
      </p>
      <p class="contact-row">
        <svg class="contact-icon" viewBox="0 0 26 26" aria-hidden="true">
          <rect x="1" y="1" width="24" height="24" rx="6" fill="none" stroke="var(--blue)" stroke-width="1.6"/>
          <rect x="6" y="8" width="14" height="10" fill="var(--blue)"/>
          <path d="M6 8l7 6 7-6" fill="none" stroke="#fff" stroke-width="1.4"/>
        </svg>
        <span>Venazacoatings.utah@brushmail.net</span>
      </p>
    </div>

    <p class="services">Custom Paint &amp; Stain, Interior &amp; Exterior, Epoxy Coatings / Garage Floors, Cabinet Refinishing, Log Staining and Refinishing.</p>

    <div class="grey-band"></div>
  </section>

  <section class="card card--back" aria-label="Business card back">
    <div class="brand">
      <span class="brand-square"></span>
      <span class="brand-name">Venaza Coatings</span>
    </div>
  </section>

</body>
</html>
```